Herb Farm - Tea Label Design

We are a small herbalist company called 'Meadowlark Tisanes' which requires a new label scheme.

Meadowlark Tisanes specializes in organic wellness teas, handmade soaps, bath and beauty products. We also offer local beeswax, pollen and an herb CSA.

Our slogan is "Ancient Remedies for Modern Life" and we frequently market ourselves as an "Apothecary & Herb Farm".

The primary use of this label will be on tins and biodegradable food grade paper bags.

We are looking for:

1) An unique universal design for our products. Something that we can put on the tea tins/bags as well as boxes in the future. To keep costs down I would like something that can be used on a variety of products by simply having the colour changed or adding the title of the product in a certain area. We have four collections. Please see the attached style guide. I particularly like the Silver Kettle Brew Co. as each type of tea is reprinted by a design. Please see their website for further clarification. I also really like their styling.

2) Label required is 8.5" x 5.25" (w - h). Bear in mind we also have dark cobalt blue jars and Brunel biodegradable bags available that this label will fit on (5570-02 as pictured)

3) We would like to see a design that is colourful, and has elements of modern simplicity yet certainly has an old world apothecary charm.

4) Please refer to our current label for product information. Not everything has to be in the same place in the new design, however all the information is required.

We will require source files in .ai and .eps (layers retained, no outlines on text, list of fonts used).

Please visit: www.meadowlarktisanes.example

We included a few favourites and the styles we prefer, but please be creative!

The label chosen could be in for a lot more design work as we expand our company. Any other input regarding packaging would be helpful.
Updates

Hello Designers!

I have posted our current label for you to review - I like it, yet I don't. You can see the level of craftsman ship brings up to artisan, and mid-high range product. The only parts I really want to keep from this label is how the brewing instructions are set out.

In terms of design, I do not want to use a photograph on the label - it is there for inspiration!

Thanks,
Meadowlark Tisanes 

Reason: I would like to see more designs, from a variety of designers for this label project.

Reason: Would like to see more designs.

Reason: In receiving designs I realized that the sizing is not ideal as it does not have ample space for the required information. I have updated the brief to reflect this and posted a working file that has the required elements. A lot of good designs, but I noticed the over use of filigree or Victorian ornamentation. I would like some ornamentation but simplicity is desired in the overall label. There was not enough designs submitted, nothing that truly wow-ed me. I hope to see more unique designs! Thanks.

Target Market(s)

30-something, retired, eco-conscious, women, mid-priced marketing, local Ontario Canada; some products will be sold at a local historical village

Industry/Entity Type

Biodegradable

Font styles to use
Decorative
Other font styles liked:
• DellaRobbia BT Bold; Foglihten No07

Requirements
Must have
• Fonts used: Dellarobbia BT Bold and Foglihten No07
Use fonts and logo design; you can use separate leaf components but fonts chosen for logo cannot change

Other fonts can be used but please use Foglihten No07 for "Meadowlark Tisanes" and Dellarobbia BT Bold for "Apothecary & Herb Farm" and for "Ancient Remedies for Modern Life".
Nice to have
• "Apothecary & Herb Farm" or slogan
Should not have
• Comic sans
clipart
Filigree or line swooshes

```html
<!DOCTYPE html>
<html lang="en">
<head>
<meta charset="utf-8">
<title>Meadowlark Tisanes – Tea Label Series</title>
<link rel="stylesheet" href="https://fonts.googleapis.com/css2?family=Cormorant+Garamond:ital,wght@0,400;0,600;1,400&family=Marcellus&family=Playball&display=swap">
<style>
  :root{
    --page:#efeeec;
    --bark:#4b3a31;
    --cream:#f4efe6;
    --muted:#d9cfc2;
    --teal:#3fb5c6;
    --teal-dark:#2a8fa0;
    --lime:#a9c73a;
    --lime-dark:#86a027;
    --orchid:#b56fb6;
    --orchid-dark:#8f4f91;
    --apricot:#f2a766;
    --apricot-dark:#d6854a;
  }
  *{box-sizing:border-box;margin:0;padding:0}
  html,body{width:1200px;height:855px;overflow:hidden;background:var(--page)}
  body{position:relative;font-family:"Cormorant Garamond",Georgia,serif;color:var(--cream)}

  .label{position:absolute;background:var(--bark);overflow:hidden;--accent:var(--teal);--accent-dark:var(--teal-dark)}
  .label--full{left:77px;top:211px;width:658px;height:411px}
  .label--strip{top:214px;width:114px;height:411px}
  .label--garden{left:764px;--accent:var(--lime);--accent-dark:var(--lime-dark)}
  .label--heath{left:889px;--accent:var(--orchid);--accent-dark:var(--orchid-dark)}
  .label--fen{left:1010px;--accent:var(--apricot);--accent-dark:var(--apricot-dark)}

  .rule{position:absolute;left:0;right:0;height:5px;border-top:2px solid var(--accent);border-bottom:1px solid var(--accent)}
  .rule--top{top:22px}
  .rule--bottom{top:384px}

  /* side columns */
  .side{position:absolute;font-size:6.6px;line-height:1.35;text-align:center;color:var(--muted)}
  .side p{margin-bottom:6px}
  .side--left{left:24px;top:40px;width:112px}
  .side--right{left:497px;top:40px;width:142px;font-size:7px}
  .side em{font-style:italic}

  .nutrition{position:absolute;left:41px;top:205px;width:95px;border:1px solid var(--muted);padding:2px 3px;font-size:5.4px;line-height:1.25;color:var(--muted)}
  .nutrition h3{font-family:"Marcellus",serif;font-weight:400;font-size:10px;border-bottom:1px solid var(--muted);padding-bottom:1px}
  .nutrition .row{display:flex;justify-content:space-between;border-bottom:0.5px solid var(--muted)}
  .nutrition .row.thick{border-bottom:2px solid var(--muted)}
  .nutrition .indent{padding-left:5px}
  .nutrition .note{margin-top:2px}

  .brew{display:grid;grid-template-columns:1fr 1fr;gap:6px 8px;margin:6px 4px 12px;font-size:8px;color:var(--cream);text-align:left}
  .brew span{display:flex;align-items:center;gap:4px}
  .brew svg{width:10px;height:10px;flex:none}

  /* centre panel, shared by all labels */
  .panel{position:absolute;top:0;width:240px;height:411px;text-align:center}
  .label--full .panel{left:208px}
  .label--strip .panel{left:18px}

  .brand{position:absolute;left:30px;top:62px;width:180px;font-family:"Marcellus",serif;font-size:31px;line-height:1.02;color:var(--cream)}

  .ribbon{position:absolute;left:0;top:190px;width:240px;height:64px}
  .ribbon svg{position:absolute;inset:0}
  .ribbon__name{position:absolute;left:40px;top:17px;width:160px;font-family:"Playball",cursive;font-size:19px;color:var(--bark);transform:rotate(-3deg);white-space:nowrap}

  .double-rule{position:absolute;top:264px;width:60px;height:4px;border-top:1px solid var(--accent);border-bottom:1px solid var(--accent)}
  .double-rule--left{left:20px}
  .double-rule--right{left:160px}
  .kind{position:absolute;left:0;top:274px;width:240px;font-family:"Marcellus",serif;font-size:16px;letter-spacing:1px;color:var(--cream)}
  .kind__sub{position:absolute;left:0;top:294px;width:240px;font-family:"Playball",cursive;font-size:12px;color:var(--accent)}
  .underline{position:absolute;left:20px;top:316px;width:200px;height:1px;background:var(--muted)}
  .blurb{position:absolute;left:14px;top:324px;width:212px;font-size:8.2px;letter-spacing:0.6px;line-height:1.3;color:var(--muted)}
  .blurb em{font-style:italic}
  .weight{position:absolute;left:0;top:367px;width:240px;font-family:"Marcellus",serif;font-size:9px;letter-spacing:2px;color:var(--cream)}
  .crest{display:inline-block;width:9px;height:11px;margin:0 12px;vertical-align:-2px;background:var(--muted);border-radius:2px}
</style>
</head>
<body>

<!-- Full label: Meadow Waltz -->
<section class="label label--full">
  <div class="rule rule--top"></div>
  <div class="rule rule--bottom"></div>

  <div class="side side--left">
    <p>Always consult a medical practitioner before trying any new herbs. Plants are medicine and should be treated as such. Stop use at once if you feel unwell and see a doctor familiar with herbal care.</p>
    <p>Expires:</p>
    <p>Blended and packaged by<br>Tallgrass Tea, Ottawa ON CANADA<br>for Meadowlark Tisanes<br>Millbrook ON K0L 0A0 CANADA</p>
    <p>For product and nutritional information visit us online at<br>www.meadowlarktisanes.example<br>info@meadowlarktisanes.example</p>
  </div>

  <div class="nutrition">
    <h3>Nutrition Facts</h3>
    <div>Serving Size 1 teaspoon (2.5 g)</div>
    <div class="row thick"><span>Servings Per Container 40</span></div>
    <div class="row"><span>Amount Per Serving</span></div>
    <div class="row"><span>Calories 0</span><span>Cal from Fat 0</span></div>
    <div class="row"><span></span><span>% Daily Value*</span></div>
    <div class="row"><span>Total Fat Less than 0g</span><span>0%</span></div>
    <div class="row indent"><span>Saturated Fat 0g</span><span>0%</span></div>
    <div class="row indent"><span>Trans Fat 0g</span><span>0%</span></div>
    <div class="row indent"><span>Polyunsaturated Fat 0g</span><span>0%</span></div>
    <div class="row indent"><span>Monounsaturated Fat 0g</span><span>0%</span></div>
    <div class="row"><span>Cholesterol 0mg</span><span>0%</span></div>
    <div class="row"><span>Sodium 0mg</span><span>0%</span></div>
    <div class="row"><span>Total Carb 0g</span><span>0%</span></div>
    <div class="row thick"><span>Protein 0g</span><span>0%</span></div>
    <div class="note">Not a significant source of dietary fiber, sugar, vitamin A and C, calcium and iron. *Percent Daily Values are based on a 2,000 calorie diet.</div>
  </div>

  <div class="panel">
    <div class="brand">Meadowlark<br>Tisanes</div>
    <div class="ribbon">
      <svg viewBox="0 0 240 64" aria-hidden="true">
        <polygon points="2,26 30,22 30,52 2,56 12,40" fill="var(--accent-dark)"/>
        <polygon points="238,6 210,10 210,40 238,36 228,20" fill="var(--accent-dark)"/>
        <polygon points="22,18 218,4 218,38 22,52" fill="var(--accent)"/>
      </svg>
      <div class="ribbon__name">Meadow Waltz</div>
    </div>
    <div class="double-rule double-rule--left"></div>
    <div class="double-rule double-rule--right"></div>
    <div class="kind">WHITE TEA</div>
    <div class="kind__sub">Floral infusion</div>
    <div class="underline"></div>
    <p class="blurb">A blend of fair-trade organic white teas <em>(Camellia sinensis)</em>, organic rose <em>(Rosa rubiginosa)</em> and organic scotch heather <em>(Calluna vulgaris)</em>.</p>
    <div class="weight">NET WT. 35 g<span class="crest" role="img" aria-label="Small crest ornament"></span>1.2 oz</div>
  </div>

  <div class="side side--right">
    <p>A gentle cup that carries the hush of open meadows, pairing soft white tea with wild rose and heather. Light, sweet and fragrant, it is a quiet pleasure that is good for you too.</p>
    <p>Ingredients: Organic white tea <em>(Camellia sinensis)</em>, organic rose petals <em>(Rosa rubiginosa)</em> and organic scotch heather <em>(Calluna vulgaris)</em>.</p>
    <p>For the best cup please follow these guidelines:</p>
    <div class="brew">
      <span><svg viewBox="0 0 10 10"><circle cx="5" cy="5" r="4.2" fill="none" stroke="currentColor" stroke-width="0.8"/><path d="M5 2.6V5h2" fill="none" stroke="currentColor" stroke-width="0.8"/></svg>2 - 3 min</span>
      <span><svg viewBox="0 0 10 10"><circle cx="5" cy="5" r="4.6" fill="var(--teal)"/><circle cx="5" cy="5" r="1.8" fill="var(--bark)"/></svg>2.5 g / 1 tsp</span>
      <span>177 mL / 6 oz</span>
      <span><svg viewBox="0 0 10 10"><path d="M5 0.8C3.6 3.4 2.4 4.8 2.4 6.4a2.6 2.6 0 0 0 5.2 0C7.6 4.8 6.4 3.4 5 0.8z" fill="var(--teal)"/></svg>80C / 176F</span>
    </div>
    <p>MEADOWLARK TISANES<br>APOTHECARY &amp; HERB FARM</p>
    <p>Our teas come from certified organic growers, our oils are purely botanical, and every wild herb is gathered with a light hand.</p>
    <p>Nothing synthetic, no added scents, dyes or fillers ever find their way into a Meadowlark Tisanes blend.</p>
    <p>Only honest herbs, grown and blended with care.</p>
    <p>Ancient Remedies for Modern Life.</p>
  </div>
</section>

<!-- Colour variants -->
<section class="label label--strip label--garden">
  <div class="rule rule--top"></div>
  <div class="rule rule--bottom"></div>
  <div class="panel">
    <div class="brand">Meadowlark<br>Tisanes</div>
    <div class="ribbon">
      <svg viewBox="0 0 240 64" aria-hidden="true">
        <polygon points="2,26 30,22 30,52 2,56 12,40" fill="var(--accent-dark)"/>
        <polygon points="22,18 218,4 218,38 22,52" fill="var(--accent)"/>
      </svg>
      <div class="ribbon__name">Garden Ramble</div>
    </div>
    <div class="double-rule double-rule--left"></div>
    <div class="kind">WHITE TEA</div>
    <div class="kind__sub">Floral infusion</div>
    <div class="underline"></div>
    <p class="blurb">A blend of fair-trade organic white teas <em>(Camellia sinensis)</em>, organic rose and organic scotch heather.</p>
    <div class="weight">NET WT. 35 g</div>
  </div>
</section>

<section class="label label--strip label--heath">
  <div class="rule rule--top"></div>
  <div class="rule rule--bottom"></div>
  <div class="panel">
    <div class="brand">Meadowlark<br>Tisanes</div>
    <div class="ribbon">
      <svg viewBox="0 0 240 64" aria-hidden="true">
        <polygon points="2,26 30,22 30,52 2,56 12,40" fill="var(--accent-dark)"/>
        <polygon points="22,18 218,4 218,38 22,52" fill="var(--accent)"/>
      </svg>
      <div class="ribbon__name">Heath Reverie</div>
    </div>
    <div class="double-rule double-rule--left"></div>
    <div class="kind">WHITE TEA</div>
    <div class="kind__sub">Floral infusion</div>
    <div class="underline"></div>
    <p class="blurb">A blend of fair-trade organic white teas <em>(Camellia sinensis)</em>, organic rose and organic scotch heather.</p>
    <div class="weight">NET WT. 35 g</div>
  </div>
</section>

<section class="label label--strip label--fen">
  <div class="rule rule--top"></div>
  <div class="rule rule--bottom"></div>
  <div class="panel">
    <div class="brand">Meadowlark<br>Tisanes</div>
    <div class="ribbon">
      <svg viewBox="0 0 240 64" aria-hidden="true">
        <polygon points="2,26 30,22 30,52 2,56 12,40" fill="var(--accent-dark)"/>
        <polygon points="22,18 218,4 218,38 22,52" fill="var(--accent)"/>
      </svg>
      <div class="ribbon__name">Fen Whisper</div>
    </div>
    <div class="double-rule double-rule--left"></div>
    <div class="kind">WHITE TEA</div>
    <div class="kind__sub">Floral infusion</div>
    <div class="underline"></div>
    <p class="blurb">A blend of fair-trade organic white teas <em>(Camellia sinensis)</em>, organic rose and organic scotch heather.</p>
    <div class="weight">NET WT. 35 g</div>
  </div>
</section>

</body>
</html>
```